Tobrin Pelmo Broth is looking for a DL Flyer for their unique food the #velmorabroth

We're looking for a punchy flyer which depicts our food dish and includes a small blurb on the front & back. Flyer size is portrait style DL (210 x 99mm) & must be 'Press Ready Files'.
Brief: Flyer background is light wooden chopping board with vertical strips.

(Text: Calibri Body or similar text, must be easy to read! Minimum 50% width)
TvR proudly present..
(Text: Calibri Body Header or similar text, must be easy to read! Min. 75% width) PELMO BROTH

Below the text PELMO BROTH insert an image (size is approx 25% of Flyer) of Borneo with a reference to Kuching. Map of Borneo can be an outline or similar but not too prominent.
Overlay the top of the map with the following text in Monotype Corsivab or similar! but must be easy to read.
Text: Kuching (2 sizes larger) Capital City of Sarawak on the Island of Borneo is home to some of the world’s greatest and unique dishes.
(new line) TvR will take you on a culinary journey to Kuching with a favourite local dish the
(new line) #VelmoraBroth (double space) so sit back, relax & enjoy!

Insert and centre the attached image DSC_0927.JPG
Remove the spoon and make the image more vibrant, do not change the colour of the soup.
Refer to attached file Flyer.jpg for images of chopsticks, a boiled egg and ingredients at the bottom. We like the lines to point to key ingredients e.g. to the egg, prawns etc. current design the font is difficult to read.

List contact details toward the bottom.
e: TvR.PelmoBroth@quillmail.example
m: +61 437152096
f : Tobrin Pelmo Broth

on the reverse of the Flyer:
Background is light wooden chopping board with vertical strips, same as front.

Refer to below link for text & Nutritional Values table.
The text for the main four paragraphs should be the key note and majority.
Note the Ingredients and the Nutritional Values table size is max 12.5% of the total Flyer size.

https://files.dorvanshare.example/doc/7QmTx83LwPzR2nVb5KcYe0HsJd4UfAi6Go1tNr9/edit

Target Market(s)

An international foody with a sense of adventure. The dish is nutritional, Gluten Free and a healthy meal. It will be sold at food markets, to office workers for lunch and for a lighter evening meal.

Industry/Entity Type

Food Production

Colors

Designer to choose colors to be used in the design.

Requirements
Must have
• 'TvR proudly present..' must be a statement along with the product 'PELMO BROTH'
• The map of Borneo with reference to Kuching, the home of the product.
• A picture of the dish itself.

```html
<!DOCTYPE html>
<html lang="en">
<head>
<meta charset="utf-8">
<title>Pelmo Broth – DL Flyer</title>
<link rel="stylesheet" href="https://fonts.googleapis.com/css2?family=Carlito:ital,wght@0,400;0,700;1,400;1,700&family=Open+Sans:wght@600;700&display=swap">
<style>
  :root {
    --stage: #4d443e;
    --panel-dark: #161616;
    --panel-mid: #262626;
    --accent: #f7b21b;
    --ink: #ffffff;
    --ink-soft: #e8e8e8;
    --map-tone: #3b3b3b;
    --map-edge: #303030;
    --plate: #e9e7e4;
    --broth: #9a4a22;
  }
  * { margin: 0; padding: 0; box-sizing: border-box; }
  html, body { width: 1200px; height: 1200px; overflow: hidden; }
  body {
    background: var(--stage);
    font-family: "Carlito", "Calibri", sans-serif;
    color: var(--ink);
    position: relative;
  }
  .flyer {
    position: absolute;
    top: 76px;
    width: 467px;
    height: 1048px;
    background: linear-gradient(90deg, var(--panel-dark), var(--panel-mid) 50%, var(--panel-dark));
    overflow: hidden;
  }
  .flyer--front { left: 111px; }
  .flyer--back { left: 639px; }
  .abs { position: absolute; }

  /* front */
  .presents {
    top: 28px; left: 0; width: 100%;
    text-align: center;
    font-family: "Open Sans", sans-serif;
    font-weight: 700; font-size: 30px;
  }
  .title-band {
    top: 69px; left: 0; width: 100%; height: 62px;
    background: var(--accent);
    color: #111;
    font-family: "Open Sans", sans-serif;
    font-weight: 700; font-size: 54px; line-height: 62px;
    text-align: center; letter-spacing: 0.5px;
  }
  .map-area {
    top: 138px; left: 28px; width: 250px; height: 280px;
    border-radius: 38% 62% 48% 52% / 30% 45% 55% 70%;
    background: linear-gradient(160deg, var(--map-tone), var(--map-edge) 70%, rgba(48,48,48,0.4));
  }
  .intro { left: 89px; top: 151px; width: 356px; font-size: 17px; line-height: 20px; }
  .intro-lead {
    position: absolute; left: 0; top: -2px;
    font-family: "Open Sans", sans-serif; font-weight: 700; font-size: 19px;
  }
  .intro p { margin-left: 81px; text-align: justify; }
  .intro p + p { margin-top: 13px; }
  .pin { left: 49px; top: 226px; }
  .pin-label {
    left: 87px; top: 255px;
    color: var(--accent); font-family: "Open Sans", sans-serif; font-weight: 700; font-size: 17px;
  }
  .bowl {
    left: 23px; top: 356px; width: 422px; height: 422px; border-radius: 50%;
    background: radial-gradient(circle at 50% 52%, #c98a4e 0%, var(--broth) 42%, #6e3216 58%, var(--plate) 60%, #cfcbc6 100%);
  }
  .callouts { left: 0; top: 0; }
  .callout-label { font-size: 15.5px; color: var(--ink); }
  .label-chicken { left: 15px; top: 742px; }
  .label-egg { left: 55px; top: 793px; text-align: center; line-height: 16px; }
  .label-prawns { left: 373px; top: 738px; }
  .label-curd { left: 304px; top: 784px; }
  .vegan-note {
    top: 832px; left: 0; width: 100%; text-align: center;
    color: var(--accent); font-family: "Open Sans", sans-serif; font-weight: 600; font-size: 18px;
  }
  .contact-tag {
    top: 869px; left: 161px; width: 145px; height: 16px;
    background: var(--accent); color: #111;
    font-size: 14.5px; line-height: 16px; text-align: center; font-weight: 700;
  }
  .contact-list {
    top: 893px; left: 0; width: 100%;
    list-style: none; text-align: center;
    color: var(--accent); font-size: 18px; line-height: 23px;
  }
  .contact-list svg { vertical-align: -2px; margin-right: 4px; }
  .social-dot {
    display: inline-block; width: 13px; height: 13px; border-radius: 50%;
    border: 1.5px solid var(--accent); margin-right: 5px; vertical-align: -1px;
  }
  .produce-left {
    left: 0; top: 880px; width: 110px; height: 168px;
    background: linear-gradient(160deg, #7fa64a, #c9b26a 60%, #d9a13a);
  }
  .produce-right {
    left: 405px; top: 870px; width: 62px; height: 178px;
    background: linear-gradient(200deg, #e7e3da, #5f9e3e 55%, #2f7a2a);
  }
  .produce-bottom {
    left: 110px; top: 1000px; width: 295px; height: 48px;
    background: linear-gradient(90deg, #c98a4e, #b5651d 40%, #9b1c16 75%, #3f8a34);
  }

  /* back */
  .plate {
    left: 141px; top: 20px; width: 184px; height: 184px; border-radius: 50%;
    background: radial-gradient(circle at 50% 50%, #c98a4e 0%, var(--broth) 48%, #6e3216 64%, var(--plate) 66%, #cfcbc6 100%);
  }
  .story { left: 28px; top: 225px; width: 411px; font-size: 17px; line-height: 20px; color: var(--ink-soft); }
  .story p { text-align: justify; }
  .story .gap { margin-top: 20px; }
  .story strong { color: var(--ink); }
  .ingredients-band {
    top: 714px; left: 0; width: 100%; height: 17px;
    background: var(--accent); color: #111;
    font-family: "Open Sans", sans-serif; font-weight: 700; font-size: 15px; line-height: 17px; text-align: center;
  }
  .ingredients-text {
    top: 741px; left: 44px; width: 380px;
    text-align: center; font-size: 17px; line-height: 20px; color: var(--ink-soft);
  }
  .vegan-subs {
    top: 829px; left: 0; width: 100%; text-align: center;
    color: var(--accent); font-family: "Open Sans", sans-serif; font-weight: 700; font-size: 14.5px;
  }
  .nutrition {
    top: 856px; left: 159px; width: 148px;
    border-collapse: collapse; font-size: 6px; font-weight: 700; color: var(--ink);
  }
  .nutrition td { border: 1px solid var(--accent); height: 12px; padding: 0 4px; }
  .nutrition td + td { text-align: center; width: 50px; }
</style>
</head>
<body>

<section class="flyer flyer--front">
  <div class="abs map-area" role="img" aria-label="Muted outline map of Borneo with Kuching marked"></div>
  <h2 class="abs presents">TvR Proudly Present..</h2>
  <h1 class="abs title-band">PELMO BROTH</h1>

  <div class="abs intro">
    <span class="intro-lead">Kuching</span>
    <p>Capital City of Sarawak on the Island of Borneo is home to some of the world’s greatest and unique dishes.</p>
    <p><strong>TvR</strong> will take you on a culinary journey to Kuching with a favorite local dish the <strong>#VelmoraBroth</strong>&nbsp; so sit back, relax &amp; enjoy!</p>
  </div>

  <svg class="abs pin" width="40" height="52" viewBox="0 0 40 52">
    <path d="M20 2a18 18 0 0 1 18 18c0 13-18 30-18 30S2 33 2 20A18 18 0 0 1 20 2z" fill="#f7b21b"/>
    <circle cx="20" cy="19" r="12" fill="#fff"/>
  </svg>
  <span class="abs pin-label">Kuching</span>

  <div class="abs bowl" role="img" aria-label="Photo of a bowl of broth with rice vermicelli, prawns, chicken, omelette strips, bean curd, half egg, lime and coriander"></div>

  <svg class="abs callouts" width="467" height="1048" viewBox="0 0 467 1048">
    <defs>
      <marker id="arrowhead" markerWidth="8" markerHeight="8" refX="4" refY="4" orient="auto">
        <path d="M0 0L8 4L0 8z" fill="#f7b21b"/>
      </marker>
    </defs>
    <g stroke="#fff" stroke-width="1.3" marker-end="url(#arrowhead)">
      <line x1="201" y1="472" x2="59" y2="720"/>
      <line x1="189" y1="692" x2="119" y2="769"/>
      <line x1="321" y1="576" x2="403" y2="717"/>
      <line x1="325" y1="608" x2="348" y2="765"/>
    </g>
  </svg>
  <span class="abs callout-label label-chicken">Chicken Breast</span>
  <span class="abs callout-label label-egg">Free Range Egg<br>(Optional)</span>
  <span class="abs callout-label label-prawns">King Prawns</span>
  <span class="abs callout-label label-curd">Fried Bean Curd</span>

  <p class="abs vegan-note">*Vegan Option Available</p>

  <div class="abs produce-left" role="img" aria-label="Photo of lemongrass stalks and tofu cubes"></div>
  <div class="abs produce-right" role="img" aria-label="Photo of garlic cloves and fresh mint"></div>
  <div class="abs produce-bottom" role="img" aria-label="Photo of galangal root and dried red chillies"></div>

  <h3 class="abs contact-tag">CONTACT DETAILS</h3>
  <ul class="abs contact-list">
    <li><svg width="14" height="11" viewBox="0 0 14 11"><rect x="0.75" y="0.75" width="12.5" height="9.5" rx="1.5" fill="none" stroke="#f7b21b" stroke-width="1.5"/><path d="M1 1l6 5 6-5" fill="none" stroke="#f7b21b" stroke-width="1.5"/></svg>TvR.PelmoBroth@quillmail.example</li>
    <li><svg width="14" height="14" viewBox="0 0 14 14"><path d="M3 1l2.5 3-1.5 1.5a8 8 0 0 0 4.5 4.5L10 8.5l3 2.5-1.5 2.5C6 13 1 8 .5 2.5z" fill="none" stroke="#f7b21b" stroke-width="1.3"/></svg>+61 437152096</li>
    <li><span class="social-dot"></span>Tobrin Pelmo Broth</li>
  </ul>
</section>

<section class="flyer flyer--back">
  <div class="abs plate" role="img" aria-label="Photo of the broth bowl seen from above"></div>

  <div class="abs story">
    <p>From <strong>Sarawak to Sydney</strong> a short while ago on my travels around Borneo I was introduced to a place called Kuching, Capital City of Sarawak.</p>
    <p>I was overwhelmed by their number of unique dishes, from the Sea to the Borneo Jungle local sustainable ingredients are sourced to create some of Kuching’s indigenous foods.</p>
    <p class="gap">I was astonished to learn that famous Kuching dishes like Kolo Mee and the<br><strong>#VelmoraBroth</strong> are <em>breakfast dishes</em> and often sold out by 10am.</p>
    <p class="gap">I have chosen the Pelmo Broth to share with You!</p>
    <p>It converts perfectly to our requirements - a healthy, Gluten-Free nourishing meal, although maybe not breakfast for <em>everyone!</em></p>
    <p class="gap">The broth sambal / base stock is made from ALL plant-based ingredients.</p>
    <p>We add a dash of coconut milk to bring balance to this simple yet complex dish; with its’ more subtle and fine blend of aromatic herbs and spices and a hint of sour and chilli undertones.</p>
  </div>

  <h3 class="abs ingredients-band">INGREDIENTS</h3>
  <p class="abs ingredients-text">Ingredients: rice vermicelli- bihoon, omelette strips (free range eggs), sliced chicken breast, King prawns, bean-sprouts, fried bean curd and garnished with lime wedge, fresh coriander and sambal on the side.</p>
  <p class="abs vegan-subs">*VEGAN SUBSTITUTES – IF APPLICABLE</p>

  <div class="abs produce-left" role="img" aria-label="Photo of lemongrass stalks and tofu cubes"></div>
  <div class="abs produce-right" role="img" aria-label="Photo of garlic cloves and fresh mint"></div>
  <div class="abs produce-bottom" role="img" aria-label="Photo of galangal root and dried red chillies"></div>

  <table class="abs nutrition">
    <tr><td>NUTRITION INFORMATION</td><td>Pelmo Broth</td></tr>
    <tr><td></td><td>Per Serve</td></tr>
    <tr><td>ENERGY</td><td>1920kJ</td></tr>
    <tr><td>CALORIES</td><td>458</td></tr>
    <tr><td>PROTEIN</td><td>30g</td></tr>
    <tr><td>- GLUTEN</td><td>UNDETECTED</td></tr>
    <tr><td>FAT - TOTAL</td><td>38g</td></tr>
    <tr><td>CARBOHYDRATES</td><td>52g</td></tr>
  </table>
</section>

</body>
</html>
```